Postcard Design www.steadfieldclaimsdesk.com

We need a new postcard design that would show our over 25 years of knowledge and expertise, yet touch on the functions and services we can perform, in Medical Billing. The problem is that the competition is fierce, with many many new Medical Billing Companies getting in the act. Unfortunately these companies can be extremely hurtful to the financial well being of medical providers, as they do not know the laws, regulations, nor have the expertise.
Updates

I just received my final approval on my trademark, so the phrase Where Patience Pays & Precision Prevails is now a registered trademark. Also I just realized on my original postcard there is a typo. It should read Over 25 years in claims, billing, and revenue recovery, the "the" should not be there. Also I would like the "free 10 chart/EOB audit" to be a bigger deal that would catch the readers eye, maybe an expiration date or some other "call to action"

Target Market(s)

Target business is medical professionals. Chiropractors, Home Health providers, providers that would have large insurance clientele (Vitacover, PPO).
NOT targeting Familiy Practice, Pediatricians, Hospitals, Dentists.

Industry/Entity Type

Financial

Font styles to use
Serif
Sans Serif

Colors
ec1f27
3277b5
ffffff

Requirements
Must have
• New ideas not just copied from my existing postcard. Something that somehow tells the story of going with inexperience can cost you.

```html
<!DOCTYPE html>
<html lang="en">
<head>
<meta charset="utf-8">
<title>Steadfield Claims Desk – Postcard</title>
<link rel="stylesheet" href="https://fonts.googleapis.com/css2?family=Cinzel:wght@400;700&family=Open+Sans:wght@400;700;800&family=Roboto+Condensed:wght@700&display=swap">
<style>
  :root{
    --red:#ec1f27;
    --red-dark:#b5121a;
    --blue:#3277b5;
    --blue-deep:#1c3f8f;
    --blue-mid:#2a5aaa;
    --white:#ffffff;
    --ink:#1b2a4a;
    --grey:#9aa6b8;
    --page:#e6e8eb;
  }
  *{box-sizing:border-box;margin:0;padding:0}
  html,body{width:852px;height:1200px;overflow:hidden;background:var(--page)}
  body{position:relative;font-family:"Open Sans",Arial,sans-serif}

  .card{position:absolute;left:46px;width:760px;height:560px;overflow:hidden;background:var(--white);box-shadow:0 4px 14px rgba(0,0,0,.18)}
  .card--front{top:20px}
  .card--back{top:620px}
  .card svg.shapes{position:absolute;inset:0}

  /* front */
  .hero-photo{position:absolute;left:0;top:0;width:760px;height:420px;
    background:linear-gradient(100deg,#f4f6f9 0%,#dfe6ee 40%,#c9d6e6 62%,#eef1f5 100%)}
  .brand{position:absolute;left:34px;top:34px}
  .brand__name{display:flex;align-items:center;gap:10px;font-family:"Cinzel",Georgia,serif;font-weight:400;font-size:23px;line-height:1.1;color:var(--ink)}
  .brand__dot{width:14px;height:14px;border-radius:50%;background:var(--red);flex:none}
  .brand__rule{width:300px;height:2px;background:var(--red);margin:6px 0 4px 24px}
  .brand__tagline{margin-left:24px;font-family:Georgia,"Times New Roman",serif;font-size:12px;color:var(--ink)}

  .cost-chart{position:absolute;left:34px;top:116px;width:300px;padding:10px 14px 12px;background:rgba(255,255,255,.9);
    border-left:4px solid var(--red);box-shadow:0 2px 8px rgba(0,0,0,.12)}
  .cost-chart__title{font-weight:800;font-size:12px;letter-spacing:.04em;text-transform:uppercase;color:var(--red);margin-bottom:8px}
  .cost-chart__row{display:flex;align-items:center;gap:8px;margin-bottom:6px;font-size:11px;font-weight:700;color:var(--ink)}
  .cost-chart__label{width:92px;flex:none;line-height:1.15}
  .cost-chart__track{flex:1;height:14px;background:#e3e8ef;position:relative}
  .cost-chart__bar{position:absolute;left:0;top:0;bottom:0}
  .cost-chart__bar--weak{width:62%;background:var(--grey)}
  .cost-chart__bar--strong{width:96%;background:var(--blue-mid)}
  .cost-chart__value{width:30px;flex:none;text-align:right}
  .cost-chart__note{font-size:11px;color:var(--ink);margin-top:2px}
  .cost-chart__note b{color:var(--red)}

  .badge{position:absolute;left:40px;top:266px;width:176px;height:176px;border-radius:50%;
    background:var(--white);border:6px solid var(--red);display:flex;align-items:center;justify-content:center}
  .badge__inner{width:148px;height:148px;border-radius:50%;background:var(--blue-mid);color:var(--white);
    display:flex;flex-direction:column;align-items:center;justify-content:center;text-align:center}
  .badge__over{font-weight:800;font-size:19px;line-height:1}
  .badge__num{font-weight:800;font-size:66px;line-height:.9;color:var(--red);margin:2px 0 -2px}
  .badge__years{font-weight:800;font-size:22px;line-height:1;color:var(--red)}
  .badge__exp{font-weight:700;font-size:12px;margin-top:4px}
  .headline{position:absolute;left:48px;top:454px;font-family:"Cinzel",Georgia,serif;font-weight:700;line-height:1.1;text-shadow:0 2px 3px rgba(0,0,0,.3)}
  .headline__top{display:block;font-size:31px;color:var(--white)}
  .headline__bottom{display:block;font-size:36px;color:var(--red)}

  /* back */
  .perks{position:absolute;left:30px;top:22px;list-style:none;color:var(--white);font-weight:700;font-size:15.5px;line-height:1.3}
  .perks li{display:flex;gap:8px;margin-bottom:10px}
  .perks svg{flex:none;margin-top:4px}
  .ribbon{position:absolute;left:0;top:164px;width:440px;height:76px;background:var(--red);
    border-radius:0 16px 16px 0;box-shadow:0 3px 6px rgba(0,0,0,.3);padding:8px 0 0 32px;
    font-family:"Roboto Condensed","Arial Narrow",sans-serif;font-weight:700;text-transform:uppercase;line-height:1.15}
  .ribbon__top{display:block;font-size:27px;color:var(--ink)}
  .ribbon__bottom{display:block;font-size:25px;color:var(--white)}
  .facts{position:absolute;left:30px;top:262px;display:flex;gap:22px;list-style:none;font-weight:700;font-size:14.5px;line-height:1.3;color:var(--white)}
  .facts li{display:flex;gap:8px;width:186px}
  .facts li::before{content:"";flex:none;width:8px;height:8px;border-radius:50%;background:var(--red);margin-top:6px}
  .rule{position:absolute;left:30px;width:350px;height:1px;background:rgba(255,255,255,.8)}
  .pitch{position:absolute;left:30px;top:382px;font-family:"Cinzel",Georgia,serif;line-height:1.15}
  .pitch__light{display:block;font-size:15px;color:var(--white)}
  .pitch__red{display:block;font-size:22px;font-weight:700;color:var(--red)}
  .pitch__big{font-size:27px}
  .contact{position:absolute;left:30px;top:510px;display:flex;gap:30px;color:var(--white);font-weight:700;font-size:13px;line-height:1.3;text-transform:uppercase}
  .contact__item{display:flex;gap:8px}
  .contact svg{flex:none;margin-top:2px}

  .offer{position:absolute;left:392px;top:336px;width:194px;height:194px;border-radius:50%;background:var(--white);
    border:7px solid var(--red);display:flex;flex-direction:column;align-items:center;justify-content:center;text-align:center;color:var(--blue-deep);box-shadow:0 4px 10px rgba(0,0,0,.3)}
  .offer__cta{font-weight:800;font-size:11px;letter-spacing:.06em;text-transform:uppercase;color:var(--blue-deep)}
  .offer__free{font-weight:800;font-size:48px;line-height:1;color:var(--red)}
  .offer__what{font-weight:800;font-size:13px;line-height:1.2}
  .offer__expires{margin-top:6px;padding:3px 8px;background:var(--blue-deep);color:var(--white);font-weight:700;font-size:10.5px;text-transform:uppercase;border-radius:3px}
  .stamp{position:absolute;left:634px;top:82px;width:92px;height:96px;border:1.5px solid #333}
  .address-line{position:absolute;left:604px;width:130px;height:1.5px;background:#333}
</style>
</head>
<body>

<section class="card card--front" aria-label="Postcard front">
  <div class="hero-photo" role="img" aria-label="Photo of a smiling doctor in a white coat with medical staff behind him"></div>
  <svg class="shapes" width="760" height="560" viewBox="0 0 760 560" aria-hidden="true">
    <defs>
      <linearGradient id="frontBlue" x1="0" y1="0" x2="0" y2="1">
        <stop offset="0" stop-color="#3a6cc0"/>
        <stop offset="1" stop-color="#1c3f8f"/>
      </linearGradient>
    </defs>
    <path d="M0 300 C 180 330, 420 330, 760 392 L760 560 L0 560 Z" fill="url(#frontBlue)"/>
    <path d="M200 336 C 420 346, 600 368, 760 400 L760 410 C 600 378, 420 354, 200 342 Z" fill="var(--red)"/>
  </svg>
  <div class="brand">
    <div class="brand__name"><span class="brand__dot"></span><span>Steadfield Claims Desk</span></div>
    <div class="brand__rule"></div>
    <div class="brand__tagline">Where Patience Pays &amp; Precision Prevails ®</div>
  </div>

  <figure class="cost-chart" aria-label="Chart of claims collected by an inexperienced biller versus Steadfield">
    <figcaption class="cost-chart__title">What inexperience costs you</figcaption>
    <div class="cost-chart__row">
      <span class="cost-chart__label">New billing company</span>
      <span class="cost-chart__track"><span class="cost-chart__bar cost-chart__bar--weak"></span></span>
      <span class="cost-chart__value">62%</span>
    </div>
    <div class="cost-chart__row">
      <span class="cost-chart__label">25 years of expertise</span>
      <span class="cost-chart__track"><span class="cost-chart__bar cost-chart__bar--strong"></span></span>
      <span class="cost-chart__value">96%</span>
    </div>
    <p class="cost-chart__note">Every missed code is <b>money left behind.</b></p>
  </figure>

  <div class="badge">
    <div class="badge__inner">
      <span class="badge__over">OVER</span>
      <span class="badge__num">25</span>
      <span class="badge__years">YEARS</span>
      <span class="badge__exp">EXPERIENCE</span>
    </div>
  </div>
  <h1 class="headline">
    <span class="headline__top">How Much Money</span>
    <span class="headline__bottom">Is Hiding In Your Charts?</span>
  </h1>
</section>

<section class="card card--back" aria-label="Postcard back">
  <svg class="shapes" width="760" height="560" viewBox="0 0 760 560" aria-hidden="true">
    <defs>
      <linearGradient id="backBlue" x1="0" y1="0" x2="0" y2="1">
        <stop offset="0" stop-color="#2c5db0"/>
        <stop offset=".5" stop-color="#3f7fcc"/>
        <stop offset="1" stop-color="#1c3f8f"/>
      </linearGradient>
    </defs>
    <path d="M462 0 C 500 140, 520 360, 500 560 L520 560 C 540 360, 520 140, 482 0 Z" fill="var(--red)"/>
    <path d="M0 0 H448 C 486 140, 506 360, 486 560 H0 Z" fill="url(#backBlue)"/>
  </svg>

  <ul class="perks">
    <li><svg width="12" height="12" viewBox="0 0 12 12"><path d="M1 6 L4.5 9.5 L11 2" stroke="var(--red)" stroke-width="2.4" fill="none"/></svg><span>Let me recover your lost/hidden profits!</span></li>
    <li><svg width="12" height="12" viewBox="0 0 12 12"><path d="M1 6 L4.5 9.5 L11 2" stroke="var(--red)" stroke-width="2.4" fill="none"/></svg><span>Guaranteed method to increase<br>your collectibles.</span></li>
    <li><svg width="12" height="12" viewBox="0 0 12 12"><path d="M1 6 L4.5 9.5 L11 2" stroke="var(--red)" stroke-width="2.4" fill="none"/></svg><span>Let me turn your denied/delayed claims into<br>cash into your pockets!</span></li>
  </ul>

  <div class="ribbon">
    <span class="ribbon__top">Guaranteed Methods To</span>
    <span class="ribbon__bottom">Increase Your Collectibles</span>
  </div>

  <ul class="facts">
    <li><span>Over 25 years in claims, billing, and revenue recovery; PPO, HMO, Vitacover.</span></li>
    <li><span>You can't afford not to ask! ($500-$1200 VALUE)</span></li>
  </ul>

  <div class="rule" style="top:370px"></div>

  <p class="pitch">
    <span class="pitch__light">It's What You Don't Know</span>
    <span class="pitch__red">That Is Hurting You...</span>
    <span class="pitch__light">Don't Let Those Claims Go To Waste.</span>
    <span class="pitch__red pitch__big">I Can Go Get Them!</span>
  </p>

  <div class="rule" style="top:498px"></div>

  <div class="contact">
    <div class="contact__item">
      <svg width="14" height="13" viewBox="0 0 14 13"><path d="M7 0 L14 6 H12 V13 H8.5 V9 H5.5 V13 H2 V6 H0 Z" fill="var(--red)"/></svg>
      <span>4870 Larkspur Rd., # 210-118,<br>Ridgeview Falls, CA 90412</span>
    </div>
    <div class="contact__item">
      <svg width="13" height="13" viewBox="0 0 13 13"><path d="M3 0 L5 3.5 L3.6 5 C4.4 7 6 8.6 8 9.4 L9.5 8 L13 10 L11.5 12.8 C6 12.5 0.5 7 0.2 1.5 Z" fill="var(--red)"/></svg>
      <span>(800)555-0147</span>
    </div>
  </div>

  <div class="offer">
    <span class="offer__cta">Call today for your</span>
    <span class="offer__free">FREE</span>
    <span class="offer__what">10 CHART/EOB<br>AUDIT</span>
    <span class="offer__expires">Offer expires 12/31</span>
  </div>

  <div class="stamp"></div>
  <div class="address-line" style="top:300px"></div>
  <div class="address-line" style="top:322px"></div>
  <div class="address-line" style="top:344px"></div>
</section>

</body>
</html>
```